Melissa Tarnow Personal Business Card

I like orange. It's would better if my card have an orange background
Address: 4720 Halberd Lane #318
San Jose
California
US
Tel: 4085172946

Industry/Entity Type

Business

```html
<!DOCTYPE html>
<html lang="en">
<head>
<meta charset="utf-8">
<title>Melissa Tarnow – Business Card</title>
<link rel="stylesheet" href="https://fonts.googleapis.com/css2?family=Emilys+Candy&family=Quicksand:wght@500&display=swap">
<style>
  :root {
    --orange-light: #f7a06a;
    --orange-mid: #f08443;
    --orange-deep: #e96d2c;
    --text-orange: #ea7435;
    --white: #ffffff;
    --name-shadow: rgba(120, 45, 10, 0.45);
  }
  html, body {
    margin: 0;
    padding: 0;
    overflow: hidden;
    background: var(--white);
  }
  .card {
    position: relative;
    width: 1200px;
    height: 703px;
    overflow: hidden;
    background: var(--white);
  }
  .card__backdrop {
    position: absolute;
    inset: 0 0 auto 0;
    height: 440px;
    background:
      radial-gradient(circle at 22% 30%, rgba(255,255,255,0.18) 0, rgba(255,255,255,0) 28%),
      radial-gradient(circle at 78% 20%, rgba(255,255,255,0.16) 0, rgba(255,255,255,0) 30%),
      radial-gradient(circle at 55% 75%, rgba(255,255,255,0.12) 0, rgba(255,255,255,0) 30%),
      linear-gradient(160deg, var(--orange-light) 0%, var(--orange-mid) 50%, var(--orange-deep) 100%);
  }
  .card__wave {
    position: absolute;
    left: 0;
    top: 0;
    width: 1200px;
    height: 703px;
  }
  .card__name {
    position: absolute;
    margin: 0;
    font-family: "Emilys Candy", cursive;
    font-weight: 400;
    color: var(--white);
    text-shadow: 4px 5px 6px var(--name-shadow);
    line-height: 1;
    letter-spacing: 2px;
  }
  .card__name--first {
    left: 110px;
    top: 60px;
    font-size: 215px;
  }
  .card__name--last {
    left: 700px;
    top: 215px;
    font-size: 165px;
  }
  .card__contact {
    position: absolute;
    left: 0;
    top: 432px;
    width: 1200px;
    margin: 0;
    font-family: "Quicksand", sans-serif;
    font-weight: 500;
    font-style: normal;
    font-size: 56px;
    line-height: 66px;
    color: var(--text-orange);
    text-align: center;
    letter-spacing: 1px;
  }
</style>
</head>
<body>
  <main class="card">
    <div class="card__backdrop" role="img" aria-label="Orange background with soft out-of-focus light circles"></div>

    <svg class="card__wave" viewBox="0 0 1200 703" aria-hidden="true">
      <path fill="#ffffff"
        d="M0 388
           C 90 392, 180 420, 300 418
           C 420 416, 500 402, 560 398
           C 580 380, 590 372, 600 372
           C 610 372, 620 380, 640 398
           C 700 402, 780 416, 900 418
           C 1020 420, 1110 392, 1200 388
           L 1200 703 L 0 703 Z"/>
    </svg>

    <h1 class="card__name card__name--first">melissa</h1>
    <p class="card__name card__name--last">tarnow</p>

    <address class="card__contact">
      <span class="card__line">4720 Halberd Lane #318</span><br>
      <span class="card__line">San Jose, California</span><br>
      <span class="card__line">Tel: 4085172946</span>
    </address>
  </main>
</body>
</html>
```